Retail Pack Frozen Food Items

Hi - I would like to create a series of retail pack frozen food labels for various items. Please see the example label attacked and create an editable label file as I will be using this file for multiple products. Please include the same verbage for the safe handling with editable text. Label needs to have labels sections for the product name, establishment number , keep frozen, net weight section, Best by Date Section, Section for UPC code , and for the bottom right we can use "Packed for Corvane Foods Inc 4738 Pellow Ave Santa Clara, CA 95112" . i have also attached our logo for the upper left hand corner to use. please create one in black and white and one version using the blue logo. Again all fields will be editable as we will use this same file to create multiple labels of different products.

```html
<!DOCTYPE html>
<html lang="en">
<head>
<meta charset="UTF-8">
<title>Pork St. Louis Strips – Retail Label</title>
<link href="https://fonts.googleapis.com/css2?family=Josefin+Sans:wght@400;600;700&display=swap" rel="stylesheet">
<style>
  :root {
    --page: #ffffff;
    --label-cream: #f5f0da;
    --side-yellow: #f1e7ad;
    --side-yellow-light: #f6eec4;
    --band-orange: #e3a20d;
    --band-ink: #2b2b2b;
    --brand-blue: #2f6c9c;
    --ink: #4d4d4d;
    --ink-soft: #5e5e5e;
    --panel: #ffffff;
    --rule: #bdbdbd;
    --icon-orange: #eba316;
    --art-tone: #d9d0a8;
    --art-ink: #8f8a74;
  }
  /* Black & white version: add class "label--mono" to the label element */
  .label--mono {
    --label-cream: #ffffff;
    --side-yellow: #f2f2f2;
    --side-yellow-light: #f2f2f2;
    --band-orange: #1a1a1a;
    --band-ink: #ffffff;
    --brand-blue: #1a1a1a;
    --ink: #1a1a1a;
    --ink-soft: #1a1a1a;
    --icon-orange: #1a1a1a;
    --art-tone: #cccccc;
    --art-ink: #777777;
    --rule: #999999;
  }
  * { box-sizing: border-box; margin: 0; padding: 0; }
  html, body {
    width: 1200px; height: 1200px; overflow: hidden;
    background: var(--page);
    font-family: "Josefin Sans", sans-serif;
    color: var(--ink);
  }
  .label {
    position: absolute; left: 50px; top: 193px;
    width: 1100px; height: 813px;
    background: var(--label-cream);
    border-radius: 14px; overflow: hidden;
  }
  .brand-column {
    position: absolute; left: 0; top: 0; width: 302px; height: 100%;
    background: linear-gradient(180deg, var(--side-yellow-light), var(--side-yellow));
  }
  .brand-mark {
    position: absolute; left: 0; top: 78px; width: 302px;
    display: flex; flex-direction: column; align-items: center; gap: 14px;
  }
  .brand-mark .dot { width: 58px; height: 58px; border-radius: 50%; background: var(--brand-blue); }
  .brand-mark .name {
    font-weight: 700; font-size: 34px; color: var(--brand-blue);
    letter-spacing: 0.5px; text-align: center; line-height: 1.05;
  }
  .animal-art {
    position: absolute; left: 40px; top: 311px; width: 284px; height: 294px;
    background: radial-gradient(ellipse at 50% 50%, var(--art-tone), transparent 72%);
  }
  .fresh-lettering {
    position: absolute; left: 59px; top: 633px; width: 184px; height: 96px;
    background: radial-gradient(ellipse at 50% 50%, var(--art-ink), transparent 70%);
    opacity: 0.55;
  }
  .tagline-band {
    position: absolute; left: 0; bottom: 0; width: 302px; height: 79px;
    background: var(--band-orange);
    display: flex; align-items: center; justify-content: center;
    font-weight: 600; font-size: 26px; letter-spacing: 3px; color: var(--band-ink);
  }
  .product-title {
    position: absolute; left: 342px; top: 42px;
    font-weight: 700; font-size: 82px; line-height: 1.03; color: var(--ink);
  }
  .product-subtitle {
    position: absolute; left: 342px; top: 224px;
    font-weight: 600; font-size: 52px; color: var(--ink);
  }
  .product-facts {
    position: absolute; left: 340px; top: 308px;
    font-size: 32px; line-height: 37px; color: var(--ink-soft); letter-spacing: 0.5px;
  }
  .establishment {
    position: absolute; left: 804px; top: 492px;
    font-size: 16px; font-weight: 600; color: var(--ink-soft);
  }
  .safety-panel {
    position: absolute; left: 340px; top: 431px; width: 447px; height: 349px;
    background: var(--panel); border-radius: 10px;
    padding: 14px 22px 10px 48px; font-size: 11.5px; line-height: 1.15; color: var(--ink);
  }
  .safety-intro strong { display: block; }
  .safety-grid {
    display: grid; grid-template-columns: 1fr 1fr; margin: 12px 0 0 -28px;
    border-top: 1.5px solid var(--rule); border-bottom: 1.5px solid var(--rule);
  }
  .safety-step {
    display: flex; gap: 8px; align-items: flex-start; padding: 10px 6px 10px 0;
    min-height: 72px;
  }
  .safety-step:nth-child(odd) { border-right: 1.5px solid var(--rule); }
  .safety-step:nth-child(-n+2) { border-bottom: 1.5px solid var(--rule); }
  .safety-step:nth-child(even) { padding-left: 10px; }
  .safety-step svg { flex: 0 0 26px; margin-top: 6px; }
  .temps { margin-top: 12px; font-size: 10px; line-height: 1.15; }
  .temps strong { display: block; }
  .temps-table { display: grid; grid-template-columns: 1fr 110px; column-gap: 12px; }
  .more-info { margin-top: 14px; font-size: 9.5px; }
  .packer {
    position: absolute; left: 804px; top: 526px;
    font-size: 16px; line-height: 1.05; color: var(--ink-soft); font-style: normal;
  }
  .upc-box {
    position: absolute; left: 800px; top: 603px; width: 276px; height: 171px;
    background: var(--panel); border-radius: 10px;
    display: flex; align-items: center; justify-content: center;
    font-size: 15px; color: var(--ink-soft);
  }
</style>
</head>
<body>
  <div class="label">
    <aside class="brand-column">
      <div class="brand-mark">
        <span class="dot"></span>
        <span class="name">CORVANE<br>FOODS</span>
      </div>
      <div class="animal-art" role="img" aria-label="Engraved-style illustration of a pig's head"></div>
      <div class="fresh-lettering" role="img" aria-label="Hand-lettered word Fresh"></div>
      <div class="tagline-band">TASTY PORK</div>
    </aside>

    <h1 class="product-title">Pork St. Louis<br>Strips</h1>
    <p class="product-subtitle">(1 Inch Wide)</p>
    <div class="product-facts">
      <p>Net Weight: 2 Lbs</p>
      <p>Keep Frozen</p>
      <p>Best By: 20/04/2026</p>
    </div>

    <section class="safety-panel">
      <p class="safety-intro"><strong>Important</strong><strong>Food Safety Instructions:</strong>Raw Meat &amp; Poultry may contain bacteria that could cause illness if not handled or cooked safely. Follow these instructions to avoid illness.</p>
      <div class="safety-grid">
        <div class="safety-step">
          <svg width="26" height="16" viewBox="0 0 26 16"><path d="M1 9 Q8 3 16 5 L25 6 L24 9 L16 9 Q14 14 6 13 Z" fill="var(--icon-orange)"/></svg>
          <p><strong>Wash Hands</strong> with Soap &amp; water for 20 seconds and then <strong>Dry</strong></p>
        </div>
        <div class="safety-step">
          <svg width="26" height="26" viewBox="0 0 26 26"><rect x="8" y="9" width="10" height="16" rx="2" fill="var(--icon-orange)"/><rect x="10" y="3" width="6" height="6" fill="var(--icon-orange)"/><rect x="16" y="3" width="6" height="3" fill="var(--icon-orange)"/></svg>
          <p><strong>Clean Utensils &amp; Surfaces</strong> that contact this product with soap &amp; water and then Sanitize</p>
        </div>
        <div class="safety-step">
          <svg width="26" height="24" viewBox="0 0 26 24"><path d="M2 7 H20 M15 2 L21 7 L15 12" stroke="var(--icon-orange)" stroke-width="3" fill="none"/><path d="M24 17 H6 M11 12 L5 17 L11 22" stroke="var(--icon-orange)" stroke-width="3" fill="none"/></svg>
          <p>This product is uncooked.<br><strong>Keep separate</strong> from other foods</p>
        </div>
        <div class="safety-step">
          <svg width="26" height="26" viewBox="0 0 26 26"><rect x="11" y="1" width="4" height="18" rx="2" fill="var(--icon-orange)"/><circle cx="13" cy="21" r="4" fill="var(--icon-orange)"/></svg>
          <p><strong>Use a food Thermometer</strong> &amp; cook to temperature shown below</p>
        </div>
      </div>
      <div class="temps">
        <strong>Minimum internal temperatures:</strong>
        <div class="temps-table">
          <span>• Beef, Pork, Veal, Lamb, Steaks, Roasts &amp; Chops</span><span>145°F + 3 min rest time</span>
          <span>• Turkey, Chicken, Duck Whole pieces &amp; Ground</span><span>165°F</span>
          <span>• Ground Beef, Pork, Veal &amp; Lamb</span><span>160°F</span>
          <span>• Fish</span><span>145°F</span>
        </div>
        <p class="more-info">For more info www.safefoodinfo.org/safe</p>
      </div>
    </section>

    <p class="establishment">Est. No. 00000</p>
    <address class="packer">
      Packed for Corvane Foods Inc.<br>
      4738 Pellow Avenue, Santa Clara<br>
      CA 95112<br>
      www.corvanefoods.com/
    </address>
    <div class="upc-box">Barcode</div>
  </div>
</body>
</html>
```